A 3d printing services company "The Velvet Lattice" needs a clutter breaking business card design

The Velvet Lattice is a 3d design, animation and printing services company. We are in the B2B and B2C space. www.velvetlattice.com.sg
We have been in business for a year.
The logo is already done (the current file is attached).
We need a business card design which reflects the 3d printing and animations services of the company. A standard rectangular shape is not an option. The card can be die cut.
The card should have the colors of the logo and should have a high tech wow feel to it.
The front of the card should have my name, designation, cellphone email and website details. No need for an office address.
Name: Raghavan Kulkarni
Designation: Founder Director
Cellphone (65)91827345
email: raghavan@velvetlattice.com.sg
website: www.velvetlattice.com.sg
The back of the card should have the services we offer:
1. 3d Design and Modelling
2. 3d Animation
3. 3D Printing
The tag line is: "make your ideas real"
Am uploading the current business card files(back and front).
Target Market(s)
Business owners and C level managers in Marine, Healthcare industry
Industry/Entity Type
Printing
Contact Information for Business Card
Name: Raghavan Kulkarni
Cellphone (65)91827345
2. 3d Animation
3. 3D Printing

```html
<!DOCTYPE html>
<html lang="en">
<head>
<meta charset="utf-8">
<title>The Velvet Lattice – Services Card</title>
<link rel="stylesheet" href="https://fonts.googleapis.com/css2?family=Source+Sans+3:wght@400;600&display=swap">
<style>
  :root {
    --page: #ffffff;
    --card: #050505;
    --lime: #8dc63f;
    --service-text: #d9d9d9;
    --brand-green: #3dba4e;
    --brand-blue: #2a6fd0;
  }
  html, body {
    margin: 0;
    padding: 0;
    width: 1200px;
    height: 1198px;
    overflow: hidden;
    background: var(--page);
  }
  .card {
    position: relative;
    width: 1200px;
    height: 1198px;
    background: var(--card);
    border-radius: 48px;
    overflow: hidden;
    font-family: "Source Sans 3", "Myriad Pro", sans-serif;
  }
  .rule {
    position: absolute;
    left: 0;
    width: 100%;
    height: 16px;
    background: var(--lime);
  }
  .rule--top { top: 110px; }
  .rule--bottom { top: 1086px; }
  .tagline {
    position: absolute;
    top: 222px;
    left: 0;
    width: 100%;
    margin: 0;
    text-align: center;
    padding-left: 24px;
    box-sizing: border-box;
    font-size: 106px;
    font-weight: 400;
    line-height: 1;
    color: var(--lime);
    letter-spacing: -0.5px;
  }
  .services {
    position: absolute;
    top: 474px;
    left: 352px;
    margin: 0;
    padding: 0;
    list-style: none;
    font-size: 54px;
    font-weight: 600;
    line-height: 70px;
    color: var(--service-text);
  }
  .brand {
    position: absolute;
    top: 824px;
    left: 0;
    width: 100%;
    display: flex;
    justify-content: center;
    align-items: center;
    gap: 28px;
  }
  .brand__mark {
    width: 140px;
    height: 140px;
    border-radius: 50%;
    background: var(--brand-blue);
  }
  .brand__name {
    font-size: 56px;
    font-weight: 600;
    color: var(--brand-green);
    line-height: 1;
  }
</style>
</head>
<body>
  <div class="card">
    <div class="rule rule--top"></div>
    <h1 class="tagline">Make Your Ideas Real</h1>
    <ul class="services">
      <li>3d Design and Modelling</li>
      <li>3d Animation</li>
      <li>3D Printing</li>
    </ul>
    <div class="brand">
      <div class="brand__mark"></div>
      <span class="brand__name">The Velvet Lattice</span>
    </div>
    <div class="rule rule--bottom"></div>
  </div>
</body>
</html>
```